Web design project for exciting Australian start-up

Background
We are looking for a creative and talented web design artist to work alongside our market leading web developer.
• You will be required to create a modern and clean design theme for our website, incorporating selected rustic colour scheme elements for our exciting Australian start-up to operate within the coffee industry.
reoccurring work to be expected to flow to the successful designer.
Requirements
• c. 5 - 10 page website
• Landing page
• Log in/ out
• 404 template
• Typography is emphasised
• Please use either a) quillnest.com, b) free web fonts, c) plovra fonts
• All design elements in vector format
• Preferably with icons for each header title(i.e. about us, how it works etc) but designer have free reign over how the site looks, so might not be applicable
• All pages to be responsive
• Down to Kelvo resolution

High level visual design brief attached - additional pages to be worked from base design.

Design inspiration
• We would like to use design elements from the following sources:
http://www.plovra.com/vintel/ (Functionality)
Colour scheme refer to logo and complementary style guide

```html
<!DOCTYPE html>
<html lang="en">
<head>
<meta charset="utf-8">
<title>Roast Harbour – Dashboard</title>
<link rel="stylesheet" href="https://fonts.googleapis.com/css2?family=Open+Sans:wght@400;600&display=swap">
<style>
:root{
  --cream:#f6f5e8;
  --orange:#fd9d35;
  --charcoal:#4a4a4a;
  --ink:#3b3b3b;
  --muted:#777;
  --rule:#e4e4e4;
  --black:#000;
  --footer-link:#7a7a7a;
  --white:#fff;
}
*{box-sizing:border-box;margin:0;padding:0}
html,body{width:1200px;height:963px;overflow:hidden;background:var(--white)}
body{font-family:"Open Sans",Arial,sans-serif;color:var(--ink)}
.page{position:relative;width:1280px;height:1027px;transform:scale(.9375);transform-origin:0 0}
.abs{position:absolute}

/* header */
.site-header{left:0;top:0;width:1280px;height:82px;background:var(--cream)}
.brand{left:60px;top:10px;display:flex;align-items:center;gap:10px;height:62px}
.brand-mark{width:44px;height:44px;border-radius:50%;background:var(--orange)}
.brand-name{font-weight:600;font-size:22px;letter-spacing:1px;color:#111}
.pill{height:35px;border-radius:18px;color:var(--white);font-size:14px;display:flex;align-items:center;text-transform:uppercase}
.pill-market{left:841px;top:23px;width:128px;background:var(--charcoal);justify-content:center}
.pill-session{left:977px;top:23px;width:209px;background:var(--orange)}
.pill-session span{flex:1;text-align:center}
.pill-session span+span{border-left:1px solid rgba(255,255,255,.35)}

.section-title{color:var(--orange);font-size:24px;font-weight:400;line-height:1}

/* left column */
.photos-title{left:57px;top:124px}
.photo-slider{left:59px;top:155px;width:243px;height:157px;background:linear-gradient(135deg,#3d6a24 0%,#5a3a22 45%,#6b3f22 100%)}
.slider-arrow{top:70px;width:12px;height:18px}
.profile{left:58px;top:322px;font-size:14px;line-height:16px;color:var(--ink)}
.profile h3{font-size:19px;font-weight:600;line-height:24px}
.account{left:58px;top:403px;width:244px;height:270px;border-radius:3px;overflow:hidden;background:var(--orange)}
.account-head{height:46px;background:var(--charcoal);color:var(--white);font-size:19px;font-weight:600;padding:13px 19px 0}
.account-list{padding:26px 21px 0;color:var(--white)}
.account-list dt{font-size:18px;font-weight:600;color:#1b1b1b;line-height:22px}
.account-list dd{font-size:14px;line-height:17px;margin-bottom:20px}
.download{left:58px;top:697px;width:244px;height:76px;border-radius:3px;background:var(--charcoal);color:var(--white);font-size:20px;display:flex;align-items:center;padding-left:37px;gap:22px}
.file-icon{width:32px;height:42px;background:#c8191c;border-radius:2px}

.divider{left:343px;top:125px;width:1px;height:720px;background:var(--rule)}

/* middle */
.tenders-title{left:387px;top:124px}
.time-remaining{left:388px;top:150px;font-size:19px;font-weight:600;color:#555}
.intro{left:388px;top:199px;width:530px;font-size:14px;line-height:17px;color:#555}
.tenders-title-2{left:387px;top:315px}
.filters{left:388px;top:350px;display:flex;gap:47px;font-size:19px;color:#555}
.tender{width:247px;height:167px}
.t1{left:389px;top:405px;background:linear-gradient(135deg,#5a3520,#7a4a2b 55%,#3e2414)}
.t2{left:657px;top:405px;background:linear-gradient(160deg,#6b4a2e,#9b6a3f 50%,#2b1a10)}
.t3{left:389px;top:596px;background:radial-gradient(circle at 50% 45%,#5d8a2f 0 12%,#3e2a1e 30%,#1d1410 100%)}
.t4{left:657px;top:596px;background:linear-gradient(135deg,#2a160c,#6b3a1e 50%,#20110a)}

/* right column */
.inbox{left:975px;top:113px;width:245px;height:141px;border:1px solid var(--rule);border-radius:3px;overflow:hidden}
.inbox-head{height:36px;background:var(--charcoal);color:var(--white);font-size:19px;padding:5px 18px}
.inbox-list{list-style:none;padding:17px 0 0 17px;font-size:14px;color:#555}
.inbox-list li{display:flex;align-items:center;gap:9px;margin-bottom:13px}
.inbox-list svg{width:9px;height:10px}
.schedule{left:975px;top:282px;width:244px;height:270px;border-radius:3px;background:var(--orange);color:var(--white);padding:26px 0 0 18px}
.slot{width:190px;border-bottom:1px solid rgba(255,255,255,.45);padding-bottom:13px;margin-bottom:11px;font-size:14px;line-height:17px}
.slot:last-child{border-bottom:0}
.slot strong{display:block;font-size:19px;font-weight:400;color:#1b1b1b;line-height:24px}
.scrollbar{left:232px;top:16px;width:1px;height:238px;background:#a35a10}
.scroll-thumb{left:228px;top:30px;width:8px;height:40px;border-radius:4px;background:var(--charcoal)}
.calendar{left:975px;top:584px;width:244px;height:238px;border-radius:3px;background:var(--charcoal);color:var(--white)}
.cal-head{position:absolute;left:0;top:13px;width:244px;text-align:center;font-size:21px}
.cal-nav{top:20px;width:8px;height:13px}
.cal-grid{position:absolute;left:11px;top:56px;width:217px;display:grid;grid-template-columns:repeat(7,31px);font-size:10px;text-align:center}
.cal-grid .dow{font-size:9px;height:20px;border-bottom:1px solid var(--white);margin-bottom:4px;padding-top:2px}
.cal-grid span{height:24px;line-height:24px;position:relative}
.cal-grid .other{color:var(--orange)}
.cal-grid .today::before{content:"";position:absolute;left:3px;top:0;width:24px;height:24px;border-radius:50%;border:1.5px solid var(--white);box-sizing:border-box}
.cal-grid .selected{color:var(--charcoal)}
.cal-grid .selected::before{content:"";position:absolute;left:3px;top:0;width:24px;height:24px;border-radius:50%;background:var(--orange);z-index:-1}
.cal-grid .selected{z-index:0}

/* footer */
.site-footer{left:0;top:876px;width:1280px;height:151px;background:var(--black)}
.foot-col{top:26px;font-size:13px;line-height:15.5px;color:var(--footer-link);text-transform:uppercase}
.foot-col h4{color:var(--orange);font-size:14px;font-weight:400;margin-bottom:18px}
.join{left:987px;top:30px;display:flex;align-items:center;gap:5px;color:var(--orange);font-size:14px}
.join span{margin-right:6px}
.social{width:32px;height:32px;border-radius:50%;background:#8a8a8a}
.legal{right:61px;top:115px;font-size:12px;color:var(--footer-link)}
.legal-code{right:15px;top:115px;font-size:12px;color:var(--footer-link)}
</style>
</head>
<body>
<div class="page">

  <header class="site-header abs">
    <div class="brand abs"><span class="brand-mark"></span><span class="brand-name">ROAST HARBOUR</span></div>
    <nav>
      <div class="pill pill-market abs">Marketplace</div>
      <div class="pill pill-session abs"><span>Logged in</span><span>Logged out</span></div>
    </nav>
  </header>

  <aside>
    <h2 class="section-title photos-title abs">PHOTOS</h2>
    <div class="photo-slider abs" role="img" aria-label="Photo of roasted coffee beans on a green leaf over rustic wood">
      <svg class="slider-arrow abs" style="left:10px" viewBox="0 0 12 18"><path d="M10 1 2 9l8 8" fill="none" stroke="#fff" stroke-width="1.5"/></svg>
      <svg class="slider-arrow abs" style="right:12px" viewBox="0 0 12 18"><path d="m2 1 8 8-8 8" fill="none" stroke="#fff" stroke-width="1.5"/></svg>
    </div>
    <div class="profile abs">
      <h3>Café Lumen</h3>
      <p>Melbourne, Australia</p>
      <p>Member since [Feb, 2014]</p>
    </div>
    <section class="account abs">
      <div class="account-head">My account</div>
      <dl class="account-list">
        <dt>Email Address</dt><dd>Verified</dd>
        <dt>Café type</dt><dd>(i.e. Café, speciality coffee shop, restaurant)</dd>
        <dt>Payment details</dt><dd>Verified</dd>
      </dl>
    </section>
    <div class="download abs"><span class="file-icon"></span>Download</div>
  </aside>

  <div class="divider abs"></div>

  <main>
    <h2 class="section-title tenders-title abs">LIVE TENDERS</h2>
    <p class="time-remaining abs">Time remaining</p>
    <p class="intro abs">Buying top quality specialty coffee in huge variety is relatively straightforward (if you’re dealing with us!). This has been our business for the past decade or more. We now supply some of the top artisan coffee roasters in the world in more than 30 country markets.</p>
    <h2 class="section-title tenders-title-2 abs">LIVE TENDERS</h2>
    <div class="filters abs"><span>All</span><span>Period (x months)</span><span>Awaiting feedback (x)</span></div>
    <div class="tender t1 abs" role="img" aria-label="Coffee beans spilling from a white cup"></div>
    <div class="tender t2 abs" role="img" aria-label="Vintage coffee grinder, sack of beans and a steaming cup"></div>
    <div class="tender t3 abs" role="img" aria-label="Cupped hands holding soil with a green seedling"></div>
    <div class="tender t4 abs" role="img" aria-label="Close-up of dark roasted coffee beans"></div>
  </main>

  <aside>
    <section class="inbox abs">
      <div class="inbox-head">Inbox</div>
      <ul class="inbox-list">
        <li><svg viewBox="0 0 9 10"><path d="M0 0l9 5-9 5z" fill="#fd9d35"/></svg>Messages</li>
        <li><svg viewBox="0 0 9 10"><path d="M0 0l9 5-9 5z" fill="#fd9d35"/></svg>Saved searches</li>
      </ul>
    </section>

    <section class="schedule abs">
      <div class="slot"><strong>8 am – 11 am</strong>Delivery of order 3220x<br>Order: 20kg Wonder Beans</div>
      <div class="slot"><strong>11 am – 3 pm</strong>Delivery of order 3221y<br>Order: Sample testing Castella</div>
      <div class="slot"><strong>8 am – 11 am</strong>Delivery of order 3220x<br>Order: 20kg Wonder Beans</div>
      <div class="scrollbar abs"></div>
      <div class="scroll-thumb abs"></div>
    </section>

    <section class="calendar abs">
      <svg class="cal-nav abs" style="left:17px" viewBox="0 0 8 13"><path d="M7 1 1.5 6.5 7 12" fill="none" stroke="#fff" stroke-width="1.6"/></svg>
      <div class="cal-head">March 2014</div>
      <svg class="cal-nav abs" style="right:18px" viewBox="0 0 8 13"><path d="m1 1 5.5 5.5L1 12" fill="none" stroke="#fff" stroke-width="1.6"/></svg>
      <div class="cal-grid">
        <span class="dow">MON</span><span class="dow">TUE</span><span class="dow">WED</span><span class="dow">THU</span><span class="dow">FRI</span><span class="dow">SAT</span><span class="dow">SUN</span>
        <span class="other">30</span><span class="other">31</span><span>1</span><span>2</span><span>3</span><span>4</span><span class="today">5</span>
        <span>6</span><span>7</span><span>8</span><span>9</span><span>10</span><span>11</span><span>12</span>
        <span>13</span><span>14</span><span>15</span><span class="selected">16</span><span>17</span><span>18</span><span>19</span>
        <span>20</span><span>21</span><span>22</span><span>23</span><span>24</span><span>25</span><span>26</span>
        <span>27</span><span>28</span><span></span><span class="other">1</span><span class="other">2</span><span class="other">3</span><span class="other">4</span>
        <span class="other">5</span><span class="other">6</span><span class="other">7</span><span class="other">8</span><span class="other">9</span><span class="other">10</span><span class="other">11</span>
      </div>
    </section>
  </aside>

  <footer class="site-footer abs">
    <div class="foot-col abs" style="left:58px">
      <h4>Helpful info</h4>
      <p>About us</p><p>Media enquiries</p><p>Terms &amp; conditions</p><p>Privacy policy</p>
    </div>
    <div class="foot-col abs" style="left:231px">
      <h4>Who we are</h4>
      <p>How it works</p><p>FAQ</p><p>Contact us</p>
    </div>
    <div class="join abs"><span>JOIN US ON</span><i class="social"></i><i class="social"></i><i class="social"></i><i class="social"></i></div>
    <p class="legal abs">COPYRIGHT © 2014 ROAST HARBOUR | &nbsp;ALL RIGHTS RESERVED &nbsp;| PRIVACY POLICY</p>
    <p class="legal-code abs">Z11</p>
  </footer>

</div>
</body>
</html>
```